Process Roadmap for Interior Design Firm

We are looking to ramp up the design appeal of our current process roadmap to be very visually interesting, while staying informative and descriptive about our process.

Target Market(s)

In-house Clients

Industry/Entity Type

Interior Design Firm focused on sustainable and holistic design.

Other font styles liked:
• raleway

Requirements
Must have
• 1.) it would be nice if the graphic provided a more clear indication of the “journey” from one step to the next, so that there was a clear sense of the progression (such that we are directing the viewer) 2.). We would want it to fit on an 8.5”x11” page (the page could be horizontal when we have the Calm Compass formatted out with the testimonials) (in addition to the testimonials, we may also want to have the detailed descriptions of each step of the process presented below the graphic, so that the graphic is cleaner) 3.) ideally the graphic is clear and simple enough to also be used on our Bi-Weekly Client Updates, which will be typed updates for clients re their project budgets, schedule and scope. The Calm Compass graphic (without all the testimonials) would be at the end of the update, and would fit on the page horizontally at the bottom, perhaps in a space which is 7.5”w x 4”h or so.
Should not have
• bold or bright colors. Natural neutrals are preferred, such as the ones featured on the provided graphic.

```html
<!DOCTYPE html>
<html lang="en">
<head>
<meta charset="utf-8">
<title>ALD Calm Compass</title>
<link rel="stylesheet" href="https://fonts.googleapis.com/css2?family=Raleway:ital,wght@0,400;0,500;0,600;0,700;1,400&display=swap">
<style>
  :root{
    --backdrop:#2b2b2b;
    --paper:#ffffff;
    --gold:#b8924a;
    --sand:#e8e2d3;
    --ink:#2a2723;
    --muted:#555555;
  }
  *{box-sizing:border-box;margin:0;padding:0}
  html,body{width:1200px;height:1200px;overflow:hidden;background:var(--backdrop)}
  body{position:relative;font-family:"Raleway",sans-serif;color:var(--ink)}
  .sheet{position:absolute;left:86px;top:196px;width:1032px;height:796px;background:var(--paper);overflow:hidden}

  .brand-name{position:absolute;left:44px;top:38px;color:var(--gold);font-weight:500;font-size:16px;letter-spacing:2px;white-space:nowrap}

  .title-rule{position:absolute;left:0;top:0;width:1032px;height:110px}
  .title{position:absolute;left:402px;top:22px;color:var(--gold);font-weight:500;white-space:nowrap}
  .title .lead{font-size:27px;letter-spacing:6px;vertical-align:6px;margin-right:28px}
  .title .main{font-size:46px;letter-spacing:7px}

  .steps{position:absolute;left:43px;top:132px;width:950px;height:480px}
  .step{position:absolute;top:0;width:129px;height:474px}
  .step svg{position:absolute;left:0;top:0}
  .step-name{position:absolute;left:0;top:115px;width:129px;text-align:center;color:var(--gold);font-weight:600;font-size:16.5px;letter-spacing:.2px}
  .step-text{position:absolute;left:2px;top:214px;width:125px;text-align:center;font-size:12.8px;line-height:1.22;font-weight:500;white-space:nowrap}
  .step-text hr{border:0;border-top:1px solid var(--gold);width:86%;margin:7px auto 8px}

  .testimonials{position:absolute;left:0;top:622px;width:1032px;height:174px;background:var(--sand)}
  .testimonials-tab{position:absolute;left:0;top:0}
  .testimonials-title{position:absolute;left:386px;top:8px;width:251px;text-align:center;color:var(--gold);font-weight:700;font-size:15px;letter-spacing:4px}
  .quote{position:absolute;width:331px;height:110px}
  .quote svg{position:absolute;left:0;top:0}
  .quote-mark{position:absolute;left:24px;top:30px;color:var(--gold);font-weight:700;font-size:58px;line-height:1}
  .quote-text{position:absolute;left:80px;top:17px;font-size:13px;line-height:1.2;font-weight:500;white-space:nowrap}
  .q1{left:24px;top:21px}
  .q2{left:343px;top:51px;width:337px}
  .q3{left:673px;top:21px}
  .credit{position:absolute;right:18px;bottom:6px;font-size:9.5px;font-style:italic;color:var(--muted)}
</style>
</head>
<body>
<main class="sheet">
  <p class="brand-name">AVA LINDEN DESIGN</p>

  <svg class="title-rule" viewBox="0 0 1032 110" aria-hidden="true">
    <g fill="none" stroke="var(--gold)" stroke-width="1.3">
      <polyline points="276,0 392,96 1032,96"/>
      <polyline points="290,0 398,90 1032,90" stroke-opacity=".6"/>
    </g>
  </svg>
  <h1 class="title"><span class="lead">ALD CALM</span><span class="main">COMPASS</span></h1>

  <section class="steps">
    <div class="step" style="left:0">
      <svg width="129" height="474" viewBox="0 0 129 474" aria-hidden="true">
        <polygon points="64.5,1 128,38 128,160 64.5,201 1,160 1,38" fill="var(--paper)"/>
        <polygon points="0,126 129,126 129,431 64.5,474 0,431" fill="var(--sand)"/>
        <polygon points="64.5,1 128,38 128,160 64.5,201 1,160 1,38" fill="none" stroke="var(--gold)" stroke-width="1.6"/>
        <polygon points="64.5,11 104,34 104,80 64.5,103 25,80 25,34" fill="none" stroke="var(--gold)" stroke-width="1.3"/>
        <g fill="none" stroke="var(--gold)" stroke-width="1.6" stroke-linecap="round">
          <path d="M54,70 c-6,-2 -4,-8 0,-10 c4,-3 2,-8 2,-12 c0,-8 14,-10 16,0 c2,8 -8,10 -8,18 c0,4 -4,6 -10,4z"/>
          <path d="M62,54 c0,-4 6,-4 6,0"/>
          <path d="M78,46 l6,-4 M80,55 h7 M78,64 l6,4"/>
        </g>
      </svg>
      <div class="step-name">LISTENING</div>
      <div class="step-text"><p>Listening to our<br>clients, their land<br>&amp; their home</p><hr><p>Identifying their<br>needs, challenges,<br>wishes &amp; dreams</p></div>
    </div>

    <div class="step" style="left:136px">
      <svg width="129" height="474" viewBox="0 0 129 474" aria-hidden="true">
        <polygon points="64.5,1 128,38 128,160 64.5,201 1,160 1,38" fill="var(--paper)"/>
        <polygon points="0,126 129,126 129,431 64.5,474 0,431" fill="var(--sand)"/>
        <polygon points="64.5,1 128,38 128,160 64.5,201 1,160 1,38" fill="none" stroke="var(--gold)" stroke-width="1.6"/>
        <polygon points="64.5,11 104,34 104,80 64.5,103 25,80 25,34" fill="none" stroke="var(--gold)" stroke-width="1.3"/>
        <g fill="none" stroke="var(--gold)" stroke-width="1.6" stroke-linecap="round">
          <path d="M46,58 q18.5,-18 37,0 q-18.5,18 -37,0z"/>
          <circle cx="64.5" cy="58" r="6"/>
          <path d="M64.5,40 v-5 M52,43 l-3,-4 M77,43 l3,-4"/>
        </g>
      </svg>
      <div class="step-name">VISIONING</div>
      <div class="step-text"><p>Facilitating a<br>guided visioning<br>process to clarify<br>the deepest<br>intention, true<br>purpose &amp; highest<br>potential for their<br>home &amp; their<br>future within<br>it.</p></div>
    </div>

    <div class="step" style="left:272px">
      <svg width="129" height="474" viewBox="0 0 129 474" aria-hidden="true">
        <polygon points="64.5,1 128,38 128,160 64.5,201 1,160 1,38" fill="var(--paper)"/>
        <polygon points="0,126 129,126 129,431 64.5,474 0,431" fill="var(--sand)"/>
        <polygon points="64.5,1 128,38 128,160 64.5,201 1,160 1,38" fill="none" stroke="var(--gold)" stroke-width="1.6"/>
        <polygon points="64.5,11 104,34 104,80 64.5,103 25,80 25,34" fill="none" stroke="var(--gold)" stroke-width="1.3"/>
        <g fill="none" stroke="var(--gold)" stroke-width="1.6" stroke-linecap="round" stroke-linejoin="round">
          <rect x="50" y="38" width="26" height="36" rx="2"/>
          <path d="M54,47 l2,2 l3,-4 M63,47 h9 M54,56 l2,2 l3,-4 M63,56 h9 M54,65 l2,2 l3,-4 M63,65 h6"/>
          <circle cx="78" cy="72" r="6"/>
          <path d="M78,69 v3 h2"/>
        </g>
      </svg>
      <div class="step-name">PLANNING</div>
      <div class="step-text"><p>Turnig our client's<br>vision into a clearly<br>define scope,<br>budget &amp; timeline.</p><hr><p>Mapping out the<br>steps for making<br>their dream<br>a reality.</p><hr><p>Setting a meeting<br>schedule from<br>start to finish.</p></div>
    </div>

    <div class="step" style="left:408px">
      <svg width="129" height="474" viewBox="0 0 129 474" aria-hidden="true">
        <polygon points="64.5,1 128,38 128,160 64.5,201 1,160 1,38" fill="var(--paper)"/>
        <polygon points="0,126 129,126 129,431 64.5,474 0,431" fill="var(--sand)"/>
        <polygon points="64.5,1 128,38 128,160 64.5,201 1,160 1,38" fill="none" stroke="var(--gold)" stroke-width="1.6"/>
        <polygon points="64.5,11 104,34 104,80 64.5,103 25,80 25,34" fill="none" stroke="var(--gold)" stroke-width="1.3"/>
        <g fill="none" stroke="var(--gold)" stroke-width="1.6" stroke-linecap="round" stroke-linejoin="round">
          <path d="M50,42 l6,-6 l28,28 l-6,6z M56,48 l3,-3 M62,54 l3,-3 M68,60 l3,-3"/>
          <path d="M78,38 l6,6 l-22,22 l-9,3 l3,-9z"/>
        </g>
      </svg>
      <div class="step-name">DESIGNING</div>
      <div class="step-text"><p>Following the<br>schedule through<br>the design phases<br>from initial<br>design concepts,<br>technical drawings<br>&amp; details and the<br>selection of all<br>finishes, fixtures<br>&amp; furnishings.</p></div>
    </div>

    <div class="step" style="left:544px">
      <svg width="129" height="474" viewBox="0 0 129 474" aria-hidden="true">
        <polygon points="64.5,1 128,38 128,160 64.5,201 1,160 1,38" fill="var(--paper)"/>
        <polygon points="0,126 129,126 129,431 64.5,474 0,431" fill="var(--sand)"/>
        <polygon points="64.5,1 128,38 128,160 64.5,201 1,160 1,38" fill="none" stroke="var(--gold)" stroke-width="1.6"/>
        <polygon points="64.5,11 104,34 104,80 64.5,103 25,80 25,34" fill="none" stroke="var(--gold)" stroke-width="1.3"/>
        <g fill="none" stroke="var(--gold)" stroke-width="1.6" stroke-linecap="round" stroke-linejoin="round">
          <circle cx="64.5" cy="57" r="13"/>
          <path d="M64.5,38 v6 M64.5,70 v6 M45.5,57 h6 M77.5,57 h6 M51,43.5 l4,4 M74,66.5 l4,4 M51,70.5 l4,-4 M74,47.5 l4,-4"/>
          <path d="M59,57 l4,4 l7,-8"/>
        </g>
      </svg>
      <div class="step-name">MANAGING</div>
      <div class="step-text"><p>Coordinating with<br>clients, builders,<br>architects and<br>vendors to ensure<br>that the design is<br>executed with<br>excellence, and<br>the construction<br>and furnishings<br>are on-time and<br>on-budget</p></div>
    </div>

    <div class="step" style="left:680px">
      <svg width="129" height="474" viewBox="0 0 129 474" aria-hidden="true">
        <polygon points="64.5,1 128,38 128,160 64.5,201 1,160 1,38" fill="var(--paper)"/>
        <polygon points="0,126 129,126 129,431 64.5,474 0,431" fill="var(--sand)"/>
        <polygon points="64.5,1 128,38 128,160 64.5,201 1,160 1,38" fill="none" stroke="var(--gold)" stroke-width="1.6"/>
        <polygon points="64.5,11 104,34 104,80 64.5,103 25,80 25,34" fill="none" stroke="var(--gold)" stroke-width="1.3"/>
        <g fill="none" stroke="var(--gold)" stroke-width="1.6" stroke-linecap="round" stroke-linejoin="round">
          <path d="M48,60 h33 M51,60 c0,-12 6,-19 13.5,-19 c7.5,0 13.5,7 13.5,19 M64.5,41 v-4 M58,44 v10 M71,44 v10"/>
          <path d="M46,76 h37"/>
        </g>
      </svg>
      <div class="step-name">INSTALLING</div>
      <div class="step-text"><p>Overseeing the<br>inspection,<br>installation and<br>arrangement of<br>all furnishings,<br>lighting, artwork<br>and decorative<br>items.</p><hr><p>Taking care of<br>every last detail.</p></div>
    </div>

    <div class="step" style="left:816px">
      <svg width="129" height="474" viewBox="0 0 129 474" aria-hidden="true">
        <polygon points="64.5,1 128,38 128,160 64.5,201 1,160 1,38" fill="var(--paper)"/>
        <polygon points="0,126 129,126 129,431 64.5,474 0,431" fill="var(--sand)"/>
        <polygon points="64.5,1 128,38 128,160 64.5,201 1,160 1,38" fill="none" stroke="var(--gold)" stroke-width="1.6"/>
        <polygon points="64.5,11 104,34 104,80 64.5,103 25,80 25,34" fill="none" stroke="var(--gold)" stroke-width="1.3"/>
        <g fill="none" stroke="var(--gold)" stroke-width="1.6" stroke-linecap="round" stroke-linejoin="round">
          <rect x="48" y="54" width="8" height="20"/>
          <path d="M56,56 l8,-10 c2,-4 2,-8 5,-8 c4,0 4,6 2,12 h10 c3,0 4,3 3,5 l-3,14 c-1,3 -3,5 -6,5 h-19"/>
          <path d="M76,36 l2,-4 M82,40 l4,-2"/>
        </g>
      </svg>
      <div class="step-name">COMPLETING</div>
      <div class="step-text"><p>Fixing any<br>issues or defects.</p><hr><p>Follow up on<br>all remaining<br>items.</p><hr><p>Completing the<br>final finishing<br>touches to our<br>client's full &amp; total<br>satisfaction.</p></div>
    </div>
  </section>

  <section class="testimonials">
    <svg class="testimonials-tab" width="1032" height="40" viewBox="0 0 1032 40" aria-hidden="true">
      <polygon points="386,0 637,0 613,33 410,33" fill="var(--paper)"/>
    </svg>
    <h2 class="testimonials-title">•TESTIMONIALS•</h2>

    <div class="quote q1">
      <svg width="331" height="110" viewBox="0 0 331 110" aria-hidden="true"><polygon points="30,1 301,1 330,55 301,109 30,109 1,55" fill="none" stroke="var(--paper)" stroke-width="2"/></svg>
      <span class="quote-mark">“</span>
      <p class="quote-text">Lorem ipsum dolor sit amet,<br>consectetur adipiscing elit.<br>Sed volutpat pretium pharetra.<br>Maecenas porta diam justo, vitae<br>hendrerit nisi commodo et.</p>
    </div>
    <div class="quote q2">
      <svg width="337" height="110" viewBox="0 0 337 110" aria-hidden="true"><polygon points="30,1 307,1 336,55 307,109 30,109 1,55" fill="none" stroke="var(--paper)" stroke-width="2"/></svg>
      <span class="quote-mark">“</span>
      <p class="quote-text">Lorem ipsum dolor sit amet,<br>consectetur adipiscing elit.<br>Sed volutpat pretium pharetra.<br>Maecenas porta diam justo, vitae<br>hendrerit nisi commodo et.</p>
    </div>
    <div class="quote q3">
      <svg width="331" height="110" viewBox="0 0 331 110" aria-hidden="true"><polygon points="30,1 301,1 330,55 301,109 30,109 1,55" fill="none" stroke="var(--paper)" stroke-width="2"/></svg>
      <span class="quote-mark">“</span>
      <p class="quote-text">Lorem ipsum dolor sit amet,<br>consectetur adipiscing elit.<br>Sed volutpat pretium pharetra.<br>Maecenas porta diam justo, vitae<br>hendrerit nisi commodo et.</p>
    </div>
    <p class="credit">Icons by Linework from Iconfield.com</p>
  </section>
</main>
</body>
</html>
```